Maplerun Co. Wordpress Design Project

Need a redesign of this site: http://www.themaplerunco.example/. Client wants to highlight before and after images of refinished furniture in some way that really showcases their work. Client deals with refurbishing low, middle and high end patio furniture and wants to appeal across the board. However, their bread and butter is in high end furniture refinishing. The home page should highlight everything found on their current home page including same navigation. Please show a dropdown under Residential. Use a combination of blue, white, yellow and maybe orange colors.
Updates

Reason: Client is slow to give any feedback.

Industry/Entity Type

Residential

Requirements
Must have
• Include a mini contact form on the home page. Phone number prominently displayed. Dropdown under Residential.
Nice to have
• You may feel free to use different colors in the logo in order to make it work with the design better.

```html
<!DOCTYPE html>
<html lang="en">
<head>
<meta charset="utf-8">
<title>The Maplerun Company – Patio Furniture Repair</title>
<link href="https://fonts.googleapis.com/css2?family=Oswald:wght@400;500&family=Tinos&family=Noto+Sans&family=Arimo:wght@400;700&display=swap" rel="stylesheet">
<style>
:root{
  --blue:#2f7fcb;
  --blue-dark:#123c8f;
  --navy:#14287a;
  --yellow:#f7c51a;
  --orange:#f39c12;
  --orange-deep:#d97c06;
  --brown:#b8860b;
  --text:#222;
  --link:#1a2a8c;
  --page:#f3f3f3;
  --rule:#cfcfcf;
}
*{box-sizing:border-box;margin:0;padding:0}
html,body{width:835px;height:1200px;overflow:hidden}
body{position:relative;background:var(--page);font-family:"Noto Sans",sans-serif;color:var(--text)}
.abs{position:absolute}

.header{left:0;top:0;width:835px;height:126px;background:#fff}
.header-strip{left:0;top:0;width:835px;height:6px;background:linear-gradient(#f7b733,#f39c12)}
.phone-tab{left:532px;top:0;width:282px;height:36px;background:linear-gradient(#ffd36b,#f39c12);border-radius:0 0 30px 30px;box-shadow:0 2px 3px rgba(0,0,0,.3);font:italic 700 17px "Arimo",sans-serif;color:#2a1a00;display:flex;align-items:center;justify-content:center;gap:6px}
.phone-tab span{color:#7a4a00}
.brand-name{left:22px;top:16px;width:180px;font:700 27px/1.08 "Arimo",sans-serif;color:var(--navy)}

.nav{left:395px;top:92px;width:425px;height:34px;background:linear-gradient(#4a9be0,#1f63b3);border-radius:10px 10px 0 0;display:flex;align-items:center;justify-content:space-around;padding:0 6px;font:12.5px "Arimo",sans-serif;color:#fff}
.nav .active{color:#0a1f4c}
.dropdown{left:458px;top:126px;width:160px;background:#fff;border:1px solid #1f63b3;border-top:3px solid var(--orange);box-shadow:0 3px 6px rgba(0,0,0,.3);list-style:none;font:12px "Arimo",sans-serif;color:var(--blue-dark);z-index:5}
.dropdown li{padding:7px 12px;border-bottom:1px solid #dde6f2}
.dropdown li:last-child{border-bottom:0}

.hero{left:0;top:126px;width:835px;height:336px;background:radial-gradient(ellipse at 50% 40%,#ffd95a,#f5b400 70%,#eea400)}
.slide-frame{left:17px;top:146px;width:801px;height:282px;background:#fff;padding:6px;border:2px solid #3a3a3a}
.slide-a{left:23px;top:152px;width:394px;height:270px;background:linear-gradient(160deg,#d9dfd9,#a97c4d 60%,#7a5a38)}
.slide-b{left:417px;top:152px;width:396px;height:270px;background:linear-gradient(160deg,#b9a58a,#e9e2d6 55%,#6d6152)}
.caption{left:52px;top:362px;font:500 26px "Oswald",sans-serif;color:var(--navy);text-shadow:0 0 3px #fff,0 0 3px #fff;letter-spacing:.3px}
.pager{left:318px;top:405px;width:192px;height:27px;background:linear-gradient(#ffd86a,#f0a000);border-radius:14px 14px 4px 4px;display:flex;align-items:center;justify-content:center;gap:5px}
.pager .arr{width:18px;height:18px;border-radius:50%;background:var(--orange-deep);color:#fff;font-size:11px;display:flex;align-items:center;justify-content:center;margin:0 5px}
.pager .dot{width:11px;height:11px;border-radius:50%;background:#f7c51a;border:1px solid #b97800}
.pager .dot.on{background:#333;border-color:#111}

.ba{left:15px;top:477px;width:282px;height:211px;background:#fff;border:1px solid #ccc;border-radius:8px;box-shadow:0 1px 4px rgba(0,0,0,.25)}
.ba-photo{top:6px;height:196px;width:131px}
.ba-before{left:4px;background:linear-gradient(170deg,#c9cfc9,#5e7a74 60%,#6a6d6a)}
.ba-after{left:142px;background:linear-gradient(170deg,#dcdcd8,#6f5b7a 60%,#c94a86)}
.ba-label{left:0;bottom:0;width:100%;height:32px;background:rgba(40,40,40,.75);color:#fff;font:500 16px "Oswald",sans-serif;display:flex;align-items:center;justify-content:center}
.ba-arrow{top:88px;width:24px;height:34px;background:var(--yellow);color:#333;font-size:14px;display:flex;align-items:center;justify-content:center;border:1px solid #b88a00}
.ba-arrow.l{left:2px;border-radius:0 17px 17px 0}
.ba-arrow.r{left:254px;border-radius:17px 0 0 17px}

.welcome{left:316px;top:472px;width:502px}
.welcome h1{font:400 21px "Tinos",serif;color:#111}
.welcome h2{font:400 15px "Tinos",serif;color:var(--brown);margin:2px 0 6px}
.welcome p{font-size:11.3px;line-height:15px;text-align:justify;margin-bottom:14px}
.rule{height:1px;background:var(--rule)}

.what{left:18px;top:706px;font:400 21px "Tinos",serif;color:#111}
.services{top:744px;list-style:none;font-size:10px;color:var(--link)}
.services li{height:20px;padding-left:12px;position:relative}
.services li::before{content:"»";position:absolute;left:0;top:-1px;font-size:9px}
.svc-l{left:24px}.svc-r{left:290px}

.btn-band{left:16px;width:552px;height:49px;display:flex;align-items:center;justify-content:center;font:500 21px "Oswald",sans-serif;border-radius:2px}
.btn-blue{top:868px;background:linear-gradient(#c9ecff,#4ab8ee);border:1px solid #2f8fcb;color:#163e74}
.btn-yellow{top:925px;background:linear-gradient(#fff0b0,#f7c51a);border:1px solid #d49a00;color:#3a2a00}

.quote{left:589px;top:720px;width:231px;height:253px;background:linear-gradient(#f7b733,#e58e00);border:1px solid #5a3a00;border-radius:2px}
.quote h3{position:absolute;left:20px;top:5px;font:400 18px "Oswald",sans-serif;color:#1a1a1a}
.quote h3 span{color:#fff}
.q-label{position:absolute;right:165px;font:12px/16px "Tinos",serif;color:#fff;text-align:right}
.q-field{position:absolute;left:77px;width:136px;background:#fff;border:1px solid #c47a00}
.q-btn{position:absolute;top:225px;width:63px;height:21px;background:linear-gradient(#2a5fb0,#0e2f70);color:#fff;font:700 11px "Arimo",sans-serif;display:flex;align-items:center;justify-content:center;border:1px solid #0a1f4c}

.assoc{left:16px;top:1005px;font:400 21px "Tinos",serif;color:#111}

.footer{left:0;top:1135px;width:835px;height:65px;background:linear-gradient(#ffc04d,#f39c12 40%,#f7a600);border-top:3px solid #fbd06a}
.f-nav{left:24px;top:1157px;font:10.5px "Arimo",sans-serif;color:#fff}
.f-nav span{margin:0 7px}
.f-copy{left:24px;top:1174px;font:9px "Arimo",sans-serif;color:#fff}
.follow{left:653px;top:1154px;font:17px "Tinos",serif;color:#fff}
.social{top:1148px;width:30px;height:30px;border-radius:4px;border:1px solid #fff}
</style>
</head>
<body>

<div class="abs header"></div>
<div class="abs header-strip"></div>
<div class="abs phone-tab"><span>Call Us:</span> 1-800-555-0142</div>
<div class="abs brand-name">The Maplerun Company</div>
<nav class="abs nav"><span class="active">Home</span><span>Residential</span><span>Commercial</span><span>Fabrics</span><span>About Us</span><span>Contact Us</span></nav>

<section class="abs hero"></section>
<div class="abs slide-frame"></div>
<div class="abs slide-a" role="img" aria-label="Wicker patio sofa with cushions and a wooden coffee table on a sunny porch"></div>
<div class="abs slide-b" role="img" aria-label="Bright living room with white sofas and a stone fireplace"></div>
<div class="abs caption">DON'T REPLACE....RECYCLE !</div>
<div class="abs pager"><span class="arr">&#9664;</span><span class="dot on"></span><span class="dot"></span><span class="dot"></span><span class="dot"></span><span class="dot"></span><span class="arr">&#9654;</span></div>

<ul class="abs dropdown">
  <li>Refinishing</li>
  <li>Sling Replacement</li>
  <li>Restrapping</li>
  <li>Powdercoating</li>
</ul>

<div class="abs ba">
  <div class="abs ba-photo ba-before" role="img" aria-label="Worn wicker chairs before refinishing"><div class="abs ba-label">BEFORE</div></div>
  <div class="abs ba-photo ba-after" role="img" aria-label="Refinished wicker chairs with new pink cushions"><div class="abs ba-label">AFTER</div></div>
  <div class="abs ba-arrow l">&#9664;</div>
  <div class="abs ba-arrow r">&#9654;</div>
</div>

<article class="abs welcome">
  <h1>Welcome To The Maplerun Company Patio</h1>
  <h2>Patio Furniture Repair</h2>
  <p>The Maplerun Company has been refinishing patio furniture in the Mid-Atlantic Region since 1985.&nbsp; We have helped thousands of homeowners save considerably by restoring rather than replacing.</p>
  <p>We specialize in refinishing the types of high-end pool and patio furniture which was originally built to last for generations.&nbsp; It is difficult, if not impossible, to purchase comparable quality anywhere ...... at any price.</p>
  <p>Please visit our other pages above to learn more detail of our outdoor furniture repair services or call now to receive a free estimate.</p>
  <div class="rule" style="margin-top:-2px"></div>
</article>

<h2 class="abs what">What we do?</h2>
<ul class="abs services svc-l">
  <li>Wrought Iron Refinishing</li>
  <li>Custom Patio Furniture Sling Replacement</li>
  <li>Pool Furniture Restrapping</li>
  <li>Halvorsen Chair Relacing</li>
  <li>Powdercoating</li>
</ul>
<ul class="abs services svc-r">
  <li>Patio Table Repair</li>
  <li>Cast Aluminum Repainting</li>
  <li>Advice on Care and Cleaning</li>
  <li>Free Estimates by Telephone</li>
</ul>

<div class="abs btn-band btn-blue">PICK UP &amp; DELIVERY IN CT, NY, NJ, PA, DE, MD, DC, VA</div>
<div class="abs btn-band btn-yellow">ASK FOR SEASONAL DISCOUNT</div>

<form class="abs quote">
  <h3>Ask For <span>FREE QUOTE</span></h3>
  <div class="q-label" style="top:44px">Name</div><div class="q-field" style="top:33px;height:20px"></div>
  <div class="q-label" style="top:75px">Email</div><div class="q-field" style="top:66px;height:20px"></div>
  <div class="q-label" style="top:110px">Phone</div><div class="q-field" style="top:100px;height:20px"></div>
  <div class="q-label" style="top:143px">Furniture<br>That Needs<br>Service</div><div class="q-field" style="top:135px;height:74px"></div>
  <div class="q-btn" style="left:78px">Submit</div>
  <div class="q-btn" style="left:152px">Reset</div>
</form>

<div class="abs rule" style="left:16px;top:991px;width:803px"></div>
<h2 class="abs assoc">Our Professional Associations</h2>
<div class="abs" style="left:19px;top:1045px;width:185px;height:44px;background:#fff"></div>
<div class="abs" style="left:210px;top:1048px;width:110px;height:38px;background:#e9e2d4"></div>
<div class="abs" style="left:322px;top:1042px;width:148px;height:44px;background:#f1ece4"></div>
<div class="abs" style="left:474px;top:1045px;width:124px;height:48px;background:#fff"></div>
<div class="abs" style="left:608px;top:1037px;width:118px;height:64px;background:#fbe8b8"></div>
<div class="abs" style="left:735px;top:1036px;width:78px;height:78px;border-radius:50%;background:#1f2f6a"></div>

<footer class="abs footer"></footer>
<div class="abs f-nav">Home<span>|</span>Residential<span>|</span>Commercial<span>|</span>Fabrics<span>|</span>About Us<span>|</span>Contact Us</div>
<div class="abs f-copy">The Maplerun Company © 2012 | Privacy Policy</div>
<div class="abs follow">Follow Us</div>
<div class="abs social" style="left:743px;background:#3b5a9a"></div>
<div class="abs social" style="left:780px;background:#3fa9e0"></div>

</body>
</html>
```